Modern Lawfirm Business Card Design

We're looking for a business card to incorporate the newly created logo we had made.

Ideally looking for a law firm business card demonstrating, modern, minimalist, strong/bold design.

I'm open to any design honestly, but nothing "flashy".

Target Market(s)

Immigration law, family immigration, humanitarian, general legal

Industry/Entity Type

Law Firm

Contact Information for Business Card

Please use dummy information, name, street address, city, state, phone number, email, website.

Font styles to use
Serif
Sans Serif

Requirements
Must have
• Please use dummy information, name, street address, city, state, phone number, email, website.

```html
<!DOCTYPE html>
<html lang="en">
<head>
<meta charset="utf-8">
<title>Calloway Immigration Law – Business Card</title>
<link rel="stylesheet" href="https://fonts.googleapis.com/css2?family=Oswald:wght@300&display=swap">
<style>
  :root {
    --backdrop: #bfc0c4;
    --card: #ffffff;
    --brand-blue: #1b62a1;
    --band-text: #ffffff;
  }
  * { box-sizing: border-box; margin: 0; padding: 0; }
  html, body {
    width: 1200px;
    height: 1200px;
    overflow: hidden;
    background: var(--backdrop);
  }
  .canvas {
    position: relative;
    width: 1200px;
    height: 1200px;
  }
  .business-card {
    position: absolute;
    left: 60px;
    top: 292px;
    width: 1080px;
    height: 615px;
    background: var(--card);
    font-family: "Oswald", "Arial Narrow", sans-serif;
    font-weight: 300;
    color: var(--brand-blue);
  }
  .firm-name {
    position: absolute;
    left: 0;
    right: 0;
    top: 168px;
    display: flex;
    align-items: center;
    justify-content: center;
    gap: 22px;
  }
  .firm-name__mark {
    width: 52px;
    height: 52px;
    background: var(--brand-blue);
    flex: none;
  }
  .firm-name__text {
    font-size: 58px;
    line-height: 1;
    font-weight: 300;
    letter-spacing: 0.02em;
  }
  .contact {
    position: absolute;
    left: 0;
    right: 0;
    top: 290px;
    text-align: center;
    font-size: 20px;
    line-height: 1.6;
    letter-spacing: 0.04em;
  }
  .contact__name {
    font-size: 24px;
    margin-bottom: 6px;
  }
  .web-band {
    position: absolute;
    left: 62px;
    right: 62px;
    top: 494px;
    height: 61px;
    background: var(--brand-blue);
    display: flex;
    align-items: center;
    justify-content: center;
  }
  .web-band__url {
    color: var(--band-text);
    font-size: 23px;
    letter-spacing: 0.04em;
  }
</style>
</head>
<body>
  <main class="canvas">
    <section class="business-card" aria-label="Business card front">
      <h1 class="firm-name">
        <span class="firm-name__mark" aria-hidden="true"></span>
        <span class="firm-name__text">Calloway Immigration Law</span>
      </h1>
      <address class="contact" style="font-style: normal;">
        <p class="contact__name">Daniel Reyes, Attorney at Law</p>
        <p>250 Harbor Street, Suite 400 · Springfield, IL 62701</p>
        <p>(555) 201-4380 · dreyes@callowaylaw.com</p>
      </address>
      <div class="web-band">
        <span class="web-band__url">www.callowaylaw.com</span>
      </div>
    </section>
  </main>
</body>
</html>
```